Web design review and Illustrations - Manufacturing Company

We are a manufacturing company making mechanical (forged and foundry) components for many different markets (automotive, aerospace....)

We want to improve our website to attract more visitors (original : www.vostrela.com)
We have started working on the design and have attached some templates as an inspiration but we would need the help of a professional designer to make it look more clean, modern...and professional.

There are 3 page-types following the desired flow of visitors.
- the home page
- the market level showing all the components we can produce for one market
- the component level were we detail the specifications, materials.... we are able to manufacture for one component type.

For these 3 pages we would need to improve the templates that are attached but we would like to keep the same layout.

We would also require some kind of illustrations:
- Illustrations for the home page, today we have a big casting picture that we resided but it would be nice to have something more original.
- illustrations for the market and associated components pages that would come as a head banner of the markets sections. For the automotive market and all it's components we would keep the same illustration (a car for example) and same for Aerospace market.... (attached one example head banner that could go for automotive market)

There would definitely be an opportunity for further collaboration with the selected designer since we have many sub-divisions in the group that could use some web marketing as well.

We thank you all for your help and look forward to seeing you designs.
Updates

Project Deadline Extended
Reason: refine already submitted designs

Target Market(s)

typically purchasing departments, Engineering departments... of mechanical industry companies. We supply for example Malvec, TQ... for automotive industry, Skorel for Aerospace industry...

Industry/Entity Type

Automotive

Requirements
Must have
• Professional look
Same layout and basic colours as the attached templates

```html
<!DOCTYPE html>
<html lang="en">
<head>
<meta charset="utf-8">
<title>Vostrela Group – Automotive</title>
<link href="https://fonts.googleapis.com/css2?family=Open+Sans:wght@600;700&family=Source+Sans+3:wght@300;400;600&display=swap" rel="stylesheet">
<style>
:root{
  --accent:#4a90d0;
  --accent-dark:#2f72b8;
  --link-blue:#2a6fb5;
  --text:#444;
  --text-soft:#666;
  --nav-text:#8a8a8a;
  --side-bg:#f2f2f2;
  --side-active:#e2e2e2;
  --line:#e6e6e6;
  --footer-bg:#232323;
  --footer-text:#e8e8e8;
  --footer-muted:#8c8c8c;
}
*{margin:0;padding:0;box-sizing:border-box}
html,body{width:946px;height:1200px;overflow:hidden;background:#fff}
body{position:relative;font-family:"Source Sans 3",sans-serif;color:var(--text)}
.abs{position:absolute}
.topbar{left:0;top:0;width:946px;height:3px;background:var(--accent)}
.brand{left:54px;top:16px;display:flex;align-items:center;gap:14px}
.brand-dot{width:44px;height:44px;border-radius:50%;background:var(--accent)}
.brand-name{font-family:"Open Sans",sans-serif;font-weight:700;font-size:24px;letter-spacing:1.5px;color:#222}
.nav{left:433px;top:3px;display:flex;height:55px}
.nav a{font-size:14px;color:var(--nav-text);text-decoration:none;padding:0 12px;line-height:62px;height:55px}
.nav a.current{background:var(--accent);color:#fff;padding:0 13px}
.account{left:796px;top:62px;font-size:12px;display:flex;gap:10px}
.account a{color:var(--accent);text-decoration:none}
.rule{left:64px;top:83px;width:816px;height:1px;background:var(--line)}
.flags{left:808px;top:89px;display:flex;gap:8px}
.markets{left:66px;top:124px;width:178px;height:328px;background:var(--side-bg);border-bottom:2px solid #cfcfcf;border-right:1px solid #ddd}
.markets h2{font-weight:400;font-size:20px;color:#333;padding:8px 0 0 31px;height:36px;background:linear-gradient(#f6f6f6,#ececec)}
.markets ul{list-style:none;margin-top:4px}
.markets li{height:25.4px;line-height:25.4px;padding-left:40px;font-size:12px;color:#555;position:relative}
.markets li::before{content:"";position:absolute;left:29px;top:8px;border-left:5px solid #bbb;border-top:5px solid transparent;border-bottom:5px solid transparent}
.markets li.active{background:var(--side-active)}
.refs-title{left:67px;top:488px;font-size:17px;font-weight:400;color:#333}
.refs{left:66px;top:516px;width:178px;height:325px;border:1px solid #e6e6e6;border-radius:3px}
.refs-grid{position:absolute;left:8px;top:16px;width:160px;height:290px;background:#fafafa;display:grid;grid-template-columns:repeat(3,1fr);grid-template-rows:repeat(5,1fr);align-items:center;justify-items:center}
.ref{width:36px;height:18px;border-radius:3px;background:#d4d4d4}
.banner{left:268px;top:126px;width:613px;height:168px;border-radius:3px;background:linear-gradient(180deg,#f4f4f4 0%,#dfe0e2 55%,#c9cbce 100%)}
.page-title{left:270px;top:309px;font-size:24px;font-weight:300;color:#333}
.lead{left:270px;top:345px;width:614px;font-size:12.5px;line-height:17.5px;color:var(--text-soft);font-weight:400}
.body-copy{left:270px;top:388px;width:614px;font-size:10.3px;line-height:17.6px;color:var(--text-soft)}
.cta{left:269px;top:488px;width:177px;height:33px;border-radius:3px;background:linear-gradient(#6aa8e0,var(--accent-dark));border:1px solid #2d6aa8;color:#fff;font-size:11.5px;line-height:31px;text-align:center;letter-spacing:.2px}
.group h3{font-weight:400;font-size:15.5px;color:var(--link-blue);margin-bottom:6px}
.group .item{width:162px;height:21px;margin-bottom:4px;background:#efefef;border-radius:2px;font-size:11px;color:#444;line-height:21px;padding-left:12px;position:relative}
.group .item::after{content:"";position:absolute;right:10px;top:6px;border-left:4px solid #aaa;border-top:4px solid transparent;border-bottom:4px solid transparent}
.footer-edge{left:0;top:894px;width:946px;height:6px;background:repeating-linear-gradient(45deg,#ccc 0 1px,#eee 1px 3px)}
.footer{left:0;top:900px;width:946px;height:300px;background:var(--footer-bg)}
.footer h4{font-weight:600;font-size:16px;color:var(--footer-text);position:absolute}
.footer ul{list-style:none;position:absolute}
.footer li{font-size:11px;color:var(--footer-text);line-height:20px}
.vline{width:1px;background:#444;top:28px;height:156px}
.social{left:766px;top:63px;display:flex;gap:8px}
.social span{width:19px;height:19px;border-radius:2px;background:#5b6470}
.footer-rule{left:64px;top:220px;width:816px;height:1px;background:#3e3e3e}
.copyright{left:74px;top:238px;font-size:11px;color:var(--footer-muted)}
</style>
</head>
<body>
<div class="abs topbar"></div>

<header>
  <div class="abs brand"><span class="brand-dot"></span><span class="brand-name">Vostrela Group</span></div>
  <nav class="abs nav">
    <a class="current">Home</a><a>The Group</a><a>Forging</a><a>Casting</a><a>Services</a><a>Contact</a>
  </nav>
  <div class="abs account"><a>Login</a><a>Register</a></div>
  <div class="abs rule"></div>
  <div class="abs flags">
    <svg width="16" height="11" viewBox="0 0 16 11" aria-label="Deutsch"><rect width="16" height="3.7" fill="#000"/><rect y="3.7" width="16" height="3.6" fill="#d00"/><rect y="7.3" width="16" height="3.7" fill="#fc0"/></svg>
    <svg width="16" height="11" viewBox="0 0 16 11" aria-label="Français"><rect width="5.3" height="11" fill="#0a3fa0"/><rect x="5.3" width="5.4" height="11" fill="#fff"/><rect x="10.7" width="5.3" height="11" fill="#e0202a"/></svg>
    <svg width="16" height="11" viewBox="0 0 16 11" aria-label="English"><rect width="16" height="11" fill="#1d3a8a"/><path d="M0 0L16 11M16 0L0 11" stroke="#fff" stroke-width="2.2"/><path d="M0 0L16 11M16 0L0 11" stroke="#c8102e" stroke-width=".8"/><path d="M8 0V11M0 5.5H16" stroke="#fff" stroke-width="3.2"/><path d="M8 0V11M0 5.5H16" stroke="#c8102e" stroke-width="1.8"/></svg>
  </div>
</header>

<aside>
  <div class="abs markets">
    <h2>Markets</h2>
    <ul>
      <li>Aerospace</li><li>Agriculture</li><li class="active">Automotive</li><li>Defense</li><li>Energy</li><li>Material Handling</li><li>Off Highway</li><li>Oil &amp; Gas</li><li>Railway</li><li>Ship building</li><li>Trucks</li>
    </ul>
  </div>
  <h2 class="abs refs-title">Our References</h2>
  <div class="abs refs">
    <div class="refs-grid">
      <span class="ref"></span><span class="ref"></span><span class="ref"></span>
      <span class="ref"></span><span class="ref"></span><span class="ref"></span>
      <span class="ref"></span><span class="ref"></span><span class="ref"></span>
      <span class="ref"></span><span class="ref"></span><span class="ref"></span>
      <span class="ref"></span><span class="ref"></span><span class="ref"></span>
    </div>
  </div>
</aside>

<main>
  <div class="abs banner" role="img" aria-label="Head banner: silver sports car on a light grey background"></div>
  <h1 class="abs page-title">Automotive</h1>
  <p class="abs lead">Lorem ipsum dolor sit amet, consectetuer adipiscing elit. Nam cursus. Morbi ut mi. Nullam enim leo, egestas id, condimentum at, laoreet mattis, massa.</p>
  <p class="abs body-copy">Duis tincidunt lectus quis dui viverra vestibulum. Suspendisse vulputate aliquam dui. Nulla elementum dui ut augue. Aliquam vehicula mi at mauris. Maecenas placerat, nisl at consequat rhoncus, sem nunc gravida justo, quis eleifend arcu velit quis lacus. Morbi magna magna, tincidunt a, mattis non, imperdiet vitae, tellus. Sed odio est, auctor ac, sollicitudin in, consequat vitae, orci. Fusce id felis. Vivamus sollicitudin metus eget eros.<br>Morbi porta, libero id ullamcorper nonummy, nibh ligula pulvinar metus, eget</p>
  <div class="abs cta">REQUEST FREE QUOTE NOW</div>

  <section class="abs group" style="left:268px;top:563px">
    <h3>Injection System</h3>
    <div class="item">Common rails</div>
    <div class="item">Injections</div>
  </section>
  <section class="abs group" style="left:462px;top:563px">
    <h3>Power Train</h3>
    <div class="item">Connecting rods</div>
  </section>
  <section class="abs group" style="left:659px;top:563px">
    <h3>Transmission</h3>
    <div class="item">Shafts</div>
    <div class="item">Gears</div>
  </section>
</main>

<div class="abs footer-edge"></div>
<footer class="abs footer">
  <h4 style="left:74px;top:32px">Casting</h4>
  <ul style="left:74px;top:56px"><li>Korvat (France)</li><li>Ferrolane (France)</li><li>Nonummy nibh</li><li>Kigula pulvinar</li></ul>
  <div class="abs vline" style="left:207px"></div>
  <h4 style="left:327px;top:28px">Forging - Ostrafe</h4>
  <ul style="left:231px;top:56px"><li>Ostrafe Barnel &amp; Daleaux Industries</li><li>Ostrafe Electrovane</li><li>Ostrafe Estarvo</li><li>Ostrafe Extrusion</li><li>Ostrafe Gauvel</li><li>Ostrafe Hot Formers</li></ul>
  <ul style="left:434px;top:54px"><li>Ostrafe Lhorval</li><li>Ostrafe Near Net</li><li>Ostrafe Outillages &amp; Services</li><li>Ostrafe Quest Aubrin &amp; Duvel</li><li>Ostrafe la Clairmont</li></ul>
  <div class="abs vline" style="left:604px"></div>
  <h4 style="left:632px;top:32px">Trading Talvira</h4>
  <ul style="left:632px;top:56px"><li>Talvira Chine</li><li>Talvira France</li><li>Talvira Indonesia</li></ul>
  <h4 style="left:633px;top:132px">Magnets Magnevo</h4>
  <ul style="left:633px;top:156px"><li>Magnevo Brazil</li><li>Magnevo Korea</li></ul>
  <h4 style="left:765px;top:32px">Get In Touch</h4>
  <div class="abs social"><span></span><span></span><span></span><span></span></div>
  <div class="abs footer-rule"></div>
  <p class="abs copyright">Copyright © 2013 Company Name.&nbsp; All right reseved</p>
</footer>
</body>
</html>
```